BRAVEN POWERLINE SERVICES needs a vibrant design for electrical contracting work.

I require a card design for my own electrical contracting business. I will be doing a lot of domestic and commercial work, including things such as repairs, maintenance, lighting, installations and various others. LED lighting and energy efficiency will be a big part of my business. I wish not to have childish pictures such as light bulbs in the design, but rather a smart and modern looking card which incorporates my logo colours and perhaps the same lighting strike within the faded background of the card.

Target Market(s)

Residential and Commercial property owners.

Industry/Entity Type

Electrical

Contact Information for Business Card

Dalen Voskic
EC40923
Phone Number: 0417 358 942
Email: dalen@bravenpowerline.com

Font styles to use
Serif
Sans Serif

Requirements
Must have
• My Logo and associated colours.
Nice to have
• Some form of shapes splitting the card into different colours related to the colours of my logo. Electric Blue, Silver/Grey and White.
Should not have
• Childish pictures and symbols such as light bulbs.

```html
<!DOCTYPE html>
<html lang="en">
<head>
<meta charset="utf-8">
<title>Braven Powerline Services – Business Card</title>
<link href="https://fonts.googleapis.com/css2?family=Quicksand:wght@400;700&display=swap" rel="stylesheet">
<style>
  :root {
    --backdrop: #5a5c5e;
    --card-white: #f4f4f2;
    --electric-blue: #2b4a9e;
    --electric-blue-deep: #233f8c;
    --silver-light: #e6e7e9;
    --silver-mid: #a9abae;
    --silver-dark: #7d7f82;
    --text-light: #ffffff;
    --text-soft: #d4dbef;
  }
  html, body {
    margin: 0;
    width: 1200px;
    height: 1000px;
    overflow: hidden;
    background: var(--backdrop);
  }
  .card {
    position: absolute;
    left: 150px;
    top: 230px;
    width: 900px;
    height: 540px;
    background: var(--card-white);
    overflow: hidden;
    font-family: "Quicksand", sans-serif;
    box-shadow: 0 10px 30px rgba(0,0,0,0.35);
  }
  .card__header {
    position: absolute;
    left: 0; top: 0;
    width: 100%; height: 150px;
    display: flex;
    align-items: center;
    justify-content: center;
    gap: 18px;
  }
  .brand__dot {
    width: 54px; height: 54px;
    border-radius: 50%;
    background: var(--electric-blue);
    flex: none;
  }
  .brand__name {
    color: var(--electric-blue);
    font-weight: 700;
    font-size: 40px;
    letter-spacing: 1px;
  }
  .silver-band {
    position: absolute;
    left: 0;
    width: 100%;
    height: 16px;
    background: linear-gradient(180deg, var(--silver-light) 0%, var(--silver-mid) 50%, var(--silver-dark) 100%);
  }
  .silver-band--top { top: 150px; }
  .silver-band--bottom { top: 470px; }
  .card__body {
    position: absolute;
    left: 0; top: 166px;
    width: 100%; height: 304px;
    background: linear-gradient(180deg, var(--electric-blue) 0%, var(--electric-blue-deep) 100%);
  }
  .faint-ring {
    position: absolute;
    left: 50px; top: 40px;
    width: 210px; height: 210px;
  }
  .contact {
    position: absolute;
    left: 400px; top: 30px;
    color: var(--text-light);
  }
  .contact__name {
    margin: 0;
    font-size: 36px;
    font-weight: 700;
    line-height: 1.1;
  }
  .contact__licence {
    margin: 2px 0 0;
    font-size: 30px;
    font-weight: 400;
    color: var(--text-soft);
  }
  .contact__lines {
    margin: 56px 0 0;
    padding: 0;
    list-style: none;
    font-size: 30px;
    line-height: 1.35;
  }
  .contact__label { font-weight: 700; }
</style>
</head>
<body>
  <div class="card">
    <header class="card__header">
      <span class="brand__dot"></span>
      <span class="brand__name">BRAVEN POWERLINE SERVICES</span>
    </header>
    <div class="silver-band silver-band--top"></div>
    <section class="card__body">
      <svg class="faint-ring" viewBox="0 0 210 210" aria-hidden="true">
        <circle cx="105" cy="105" r="92" fill="none" stroke="rgba(255,255,255,0.14)" stroke-width="22"/>
      </svg>
      <div class="contact">
        <h1 class="contact__name">Dalen Voskic</h1>
        <p class="contact__licence">EC40923</p>
        <ul class="contact__lines">
          <li><span class="contact__label">P:</span> 0417 358 942</li>
          <li><span class="contact__label">E:</span> dalen@bravenpowerline.com</li>
        </ul>
      </div>
    </section>
    <div class="silver-band silver-band--bottom"></div>
  </div>
</body>
</html>
```